Webdesign für Arztpraxis
Zielgruppe
Arztpraxis für Dermatologie am Lindwarte.
Lindwarte ist ein Spital/Krankenhaus hier in Basel, Schweiz.
Kunden sind in jeder Altersstufe für Hauterkrankungen.
Behandlung Chirugisch, konservativ und mit Laser.
Aufgabenstellung
Brandguide und Logo anbei
Farben: #395722 und #ABCF8A
Beispielseite, die gefällt: https://hautarztpraxis-morvel-quandt.de

```html
<!DOCTYPE html>
<html lang="de">
<head>
<meta charset="utf-8">
<title>Dermatologie am Lindwarte</title>
<link href="https://fonts.googleapis.com/css2?family=Poppins:wght@300;400;500;600;700&display=swap" rel="stylesheet">
<style>
:root{
  --green-dark:#395722;
  --green-light:#abcf8a;
  --green-pale:#e5f0da;
  --ink:#1d1d1d;
  --muted:#777;
  --faq-bg:#f3f4f6;
  --line:#dcdcdc;
}
*{box-sizing:border-box;margin:0;padding:0}
html,body{width:1200px;height:1200px;overflow:hidden;background:#fff;font-family:'Poppins',sans-serif;color:var(--ink)}
.page{position:absolute;left:446px;top:0;width:308px;height:1200px;background:#fff}
.abs{position:absolute}
.photo{position:absolute}
.hero{left:0;top:0;width:308px;height:156px;background:linear-gradient(180deg,#c9c6cc 0%,#b7b4b5 35%,#8e8f86 60%,#6d7a4d 100%)}
.hero-trees{left:190px;top:0;width:118px;height:156px;background:linear-gradient(160deg,#4f6b35,#7f9a58 60%,#5b7340)}
.header{left:43px;top:3px;width:222px;height:17px;background:#fff;border-radius:2px;box-shadow:0 1px 3px rgba(0,0,0,.15)}
.logo{position:absolute;display:flex;align-items:center;gap:2px;font-weight:400;color:var(--green-dark);line-height:1}
.logo .dot{border-radius:50%;border:1px solid var(--green-dark)}
.header .logo{left:3px;top:3px;font-size:5.5px}
.header .logo .dot{width:9px;height:9px}
.logo small{display:block;font-size:.72em}
.nav{position:absolute;left:77px;top:12px;display:flex;gap:4px;font-size:2px;font-weight:500}
.nav .on{color:var(--green-light)}
.meta{position:absolute;top:5px;font-size:1.6px;color:var(--muted);display:flex;align-items:center;gap:1px}
.ring{width:4px;height:4px;border:.4px solid var(--muted);border-radius:50%}
.btn-out{position:absolute;border:.6px solid var(--green-light);border-radius:4px;font-size:1.8px;color:var(--green-light);display:flex;align-items:center;justify-content:center;gap:3px;background:#fff}
.arrow-btn{position:absolute;width:12px;height:12px;border-radius:50%;background:rgba(255,255,255,.35);display:flex;align-items:center;justify-content:center}
.welcome{left:150px;top:35px;width:84px;height:84px;border-radius:50%;background:#fff;text-align:center;padding-top:12px}
.welcome h1{font-size:5px;font-weight:700;line-height:1.2}
.btn-solid{display:inline-block;margin-top:10px;background:var(--green-dark);color:#fff;font-size:2.2px;font-weight:600;padding:1.5px 4px;border-radius:3px}
.pill{position:absolute;top:150px;width:53px;height:13px;background:#fff;border-radius:4px;box-shadow:0 1px 2px rgba(0,0,0,.12);font-size:2.2px;font-weight:500;display:flex;align-items:center;padding:0 3px;gap:2px}
.pill .go{margin-left:auto}
.band{position:absolute;left:0;width:308px;background:var(--green-pale)}
.portrait{position:absolute;border-radius:14px 0 0 0;background:linear-gradient(180deg,#f4f1ee,#d8c3b3 55%,#2a2a2a 85%)}
.pic{position:absolute;background:linear-gradient(135deg,#d9d4cc,#9aa8b3 50%,#e8e4dc)}
.kicker{font-size:1.6px;color:var(--green-light)}
.h2{font-size:4.2px;font-weight:600}
.body{font-size:1.8px;line-height:1.45;color:#333}
.center{text-align:center}
.thumb{position:absolute;top:284px;width:37px;height:38px;border-radius:2px}
.tl{position:absolute;top:325px;font-size:1.8px;color:var(--green-light);line-height:1.6}
.tl span{display:block;color:var(--muted)}
.dots{position:absolute;display:flex;gap:1px}
.dots i{width:1.6px;height:1.6px;border-radius:50%;background:#ccc}
.dots i:first-child{background:var(--green-light)}
.nav-dot{position:absolute;width:5px;height:5px;border-radius:50%;background:#ccc}
.card{position:absolute;top:400px;width:52px;height:62px;background:#fff;border-radius:2px;box-shadow:0 1px 3px rgba(0,0,0,.12);text-align:center;padding:17px 4px 0}
.card .c-img{position:absolute;left:15px;top:-10px;width:23px;height:23px;border-radius:50%}
.card h3{font-size:2.1px;font-weight:600;margin-bottom:2px}
.card p{font-size:1.6px;line-height:1.5;color:#444}
.card .btn-out{left:14px;top:53px;width:24px;height:5px;color:#1aa8a8;border-color:#1aa8a8}
.vita{position:absolute;font-size:1.7px;line-height:1.55;color:#333}
.vita b{font-weight:600;color:var(--ink)}
.vita p{margin-bottom:3px}
.faq{left:20px;top:771px;width:267px;height:134px;background:var(--faq-bg);border-radius:3px;padding:12px 58px 0}
.faq-q{display:flex;justify-content:space-between;font-size:2.2px;font-weight:600;border-top:.4px solid var(--line);padding:3.6px 0 3.6px}
.faq-a{font-size:1.8px;line-height:1.5;color:#555;padding:0 15px 6px 4px}
.tile{position:absolute;top:936px;width:42px;height:16px;background:#f2f2f2;border-radius:2px;text-align:center;font-size:2.8px;color:#b5b5b5;padding-top:3.5px;line-height:1.2}
.post{position:absolute;top:1014px;width:70px;height:89px;background:#fff;border-radius:2px;box-shadow:0 1px 3px rgba(0,0,0,.12)}
.post .p-img{height:50px}
.post .date{position:absolute;left:4px;top:3px;width:7px;height:7px;background:var(--green-dark);color:#fff;font-size:1.5px;text-align:center;line-height:1.3;padding-top:1px}
.post h4{font-size:2px;font-weight:600;margin:4px 4px 3px;line-height:1.3}
.post p{font-size:1.7px;line-height:1.5;color:#444;margin:0 4px}
.post .more{font-size:1.7px;color:var(--green-light);margin:3px 0 0 11px}
.footer{position:absolute;left:0;top:1112px;width:308px;height:88px;background:var(--green-dark);color:#d9e8c9}
.fcol{position:absolute;top:8px;font-size:1.8px;line-height:1.75}
.fcol .t{color:var(--green-light);margin-bottom:2px}
.social{position:absolute;left:222px;top:14px;display:flex;gap:2px}
.social i{width:6px;height:6px;border-radius:50%;background:#d9e8c9}
.flogo{position:absolute;left:192px;top:1166px;width:75px;height:20px;background:#fff;padding:4px}
.flogo .logo{font-size:6px;left:4px;top:4px}
.flogo .logo .dot{width:10px;height:10px}
</style>
</head>
<body>
<main class="page">

  <section>
    <div class="photo hero" role="img" aria-label="Praxisgebäude mit weißen Flachbauten und Bäumen"></div>
    <div class="photo hero-trees" role="img" aria-label="Grüne Bäume neben dem Gebäude"></div>
    <header class="abs header">
      <div class="logo"><span class="dot"></span><span>Dermatologie<small>am Lindwarte</small></span></div>
      <nav class="nav"><span class="on">Home</span><span>Über Uns</span><span>Leistungsspektrum</span><span>Kontakt</span></nav>
      <div class="meta" style="left:118px"><span class="ring"></span><span>Mo – Fr<br>8–17 Uhr</span></div>
      <div class="meta" style="left:155px"><svg width="4" height="4" viewBox="0 0 10 10"><path d="M2 1l2 2-1 1.5a6 6 0 0 0 2.5 2.5L7 6l2 2-1.5 1.5C4 9 1 6 .5 2z" fill="none" stroke="#777" stroke-width=".8"/></svg><span>Telefon<br>061 555 0190</span></div>
      <div class="btn-out" style="left:188px;top:4px;width:29px;height:6px">Online Termin <span>→</span></div>
    </header>
    <div class="arrow-btn" style="left:8px;top:71px"><svg width="4" height="5" viewBox="0 0 4 6"><path d="M3 .5L.8 3 3 5.5" fill="none" stroke="#fff" stroke-width=".6"/></svg></div>
    <svg class="abs" style="left:293px;top:75px" width="4" height="5" viewBox="0 0 4 6"><path d="M1 .5L3.2 3 1 5.5" fill="none" stroke="#fff" stroke-width=".6"/></svg>
    <div class="abs welcome">
      <h1>Herzlich<br>willkommen<br>in der Hautarztpraxis<br>im Rosental-Quartier<br>Basel!</h1>
      <span class="btn-solid">Termin online</span>
    </div>
    <div class="pill" style="left:43px"><span>▢</span>Termine Buchen<span class="go">→</span></div>
    <div class="pill" style="left:99px"><span>✆</span>Arzt auf Abruf<span class="go">→</span></div>
    <div class="pill" style="left:156px;justify-content:center">Anfahrt<span class="go">→</span></div>
    <div class="pill" style="left:212px;justify-content:center">Öffnungszeiten<span class="go">→</span></div>
  </section>

  <section class="band" style="top:163px;height:93px">
    <div class="portrait" style="left:43px;top:11px;width:55px;height:72px" role="img" aria-label="Porträt des Praxisinhabers im dunklen Pullover"></div>
    <div class="abs" style="left:105px;top:14px;width:90px">
      <div class="kicker">Über Uns</div>
      <div class="h2" style="font-size:3.6px">Dermatologie am Lindwarte</div>
      <p class="body" style="font-size:1.6px;margin-top:1px">Dermatologie am Lindwarte ist eine moderne Praxis für allgemeine und ästhetische Dermatologie. Wir behandeln und beraten Sie bei allen Hauterkrankungen, Hautkrebs und Allergien. Wenn es darum geht, sich einfach wieder gut und schön zu fühlen in Ihrer Haut profitieren Sie von unserer Expertise in Lasermedizin und Soft-Ästhetik. Wir sind jederzeit gerne für Sie da. Kontaktieren Sie uns, um Ihre individuellen Anliegen und Fragen zu besprechen.</p>
    </div>
    <div class="btn-out" style="left:105px;top:69px;width:37px;height:6px;color:#aaa">Über uns <span>→</span></div>
    <div class="pic" style="left:202px;top:18px;width:63px;height:56px;background:linear-gradient(135deg,#e2e6e8,#7d8fa3 45%,#d6c7b5)" role="img" aria-label="Ärztin im Beratungsgespräch mit einem Patienten"></div>
  </section>

  <section>
    <div class="abs center" style="left:0;top:264px;width:308px">
      <div class="kicker">Dermatologie</div>
      <div class="h2" style="font-size:3.4px">Leistungsspektrum</div>
    </div>
    <div class="nav-dot" style="left:40px;top:302px"></div>
    <div class="nav-dot" style="left:265px;top:302px"></div>
    <div class="thumb" style="left:43px;background:linear-gradient(135deg,#e6d2c2,#b59a88)" role="img" aria-label="Untersuchung der Haut mit Dermatoskop"></div>
    <div class="thumb" style="left:89px;background:linear-gradient(135deg,#c6d4e4,#6f87a8)" role="img" aria-label="Chirurgisches Besteck im OP"></div>
    <div class="thumb" style="left:135px;background:linear-gradient(180deg,#d9ecf8,#3b8fcf)" role="img" aria-label="Lichttherapie-Gerät in Blau"></div>
    <div class="thumb" style="left:182px;background:linear-gradient(180deg,#9cc4e6,#e6eef2 60%,#9dbb7a)" role="img" aria-label="Pusteblumen auf einer Wiese"></div>
    <div class="thumb" style="left:228px;background:linear-gradient(135deg,#c7a897,#3d4d63)" role="img" aria-label="Laserbehandlung der Haut"></div>
    <div class="tl" style="left:43px">Allgemeine Dermatologie<span>mehr erfahren</span></div>
    <div class="tl" style="left:89px">Dermatochirurgie<span>mehr erfahren</span></div>
    <div class="tl" style="left:135px">Lichttherapie<span>mehr erfahren</span></div>
    <div class="tl" style="left:182px">Allergologie<span>mehr erfahren</span></div>
    <div class="tl" style="left:228px">Lasermedizin<span>mehr erfahren</span></div>
    <div class="dots" style="left:149px;top:338px"><i></i><i></i><i></i><i></i></div>
    <div class="btn-out" style="left:134px;top:345px;width:40px;height:6px">zum Leistungsspektrum <span>→</span></div>
  </section>

  <section>
    <div class="abs center" style="left:0;top:368px;width:308px">
      <div class="kicker">Dermatologie</div>
      <div class="h2" style="font-size:3.4px">Leistungsspektrum</div>
      <div class="body" style="font-size:1.5px">version 2</div>
    </div>
    <div class="nav-dot" style="left:40px;top:428px"></div>
    <div class="nav-dot" style="left:265px;top:428px"></div>
    <article class="card" style="left:43px">
      <div class="c-img" style="background:linear-gradient(135deg,#e6d2c2,#a98a78)" role="img" aria-label="Hautuntersuchung"></div>
      <h3>Allgemeine Dermatologie</h3>
      <p>Ihre Hautgesundheit ist unser oberstes Ziel. Dabei streben wir nicht nur eine kurzfristige Linderung Ihrer Beschwerden, sondern eine nachhaltige Besserung Ihrer großen und kleinen Hautprobleme an.</p>
      <div class="btn-out">mehr <span>→</span></div>
    </article>
    <article class="card" style="left:99px">
      <div class="c-img" style="background:linear-gradient(135deg,#c6d4e4,#6f87a8)" role="img" aria-label="Chirurgisches Besteck"></div>
      <h3>Dermatochirurgie</h3>
      <p>In unserer Praxis verfügen wir über einen modernen Eingriffsraum, der allen hygienischen und organisatorischen Voraussetzungen, die an ambulantes Operieren gestellt werden, entspricht.</p>
      <div class="btn-out">mehr <span>→</span></div>
    </article>
    <article class="card" style="left:156px">
      <div class="c-img" style="background:linear-gradient(180deg,#d9ecf8,#3b8fcf)" role="img" aria-label="Lichttherapie-Gerät"></div>
      <h3>Lichttherapie</h3>
      <p>Wir bieten zudem die Entfernung kosmetisch störender Hautveränderungen in unserer Praxis mittels Laserchirurgie als individuelle Gesundheitsleistung an.</p>
      <div class="btn-out">mehr <span>→</span></div>
    </article>
    <article class="card" style="left:212px">
      <div class="c-img" style="background:linear-gradient(180deg,#9cc4e6,#e6eef2 60%,#9dbb7a)" role="img" aria-label="Pusteblumen"></div>
      <h3>Allergologie</h3>
      <p>Eine klassische Allergie ist eine Überempfindlichkeitsreaktion des Körpers auf bestimmte Stoffe (Allergene). Das Immunsystem stuft den eigentlich ungefährlichen Stoff …</p>
      <div class="btn-out">mehr <span>→</span></div>
    </article>
    <div class="dots" style="left:149px;top:464px"><i></i><i></i><i></i><i></i></div>
    <div class="btn-out" style="left:137px;top:470px;width:34px;height:7px;color:#1aa8a8;border-color:#1aa8a8">Find More Services <span>→</span></div>
  </section>

  <section class="band" style="top:494px;height:256px">
    <div class="portrait" style="left:43px;top:18px;width:55px;height:71px" role="img" aria-label="Porträt des Praxisinhabers im dunklen Pullover"></div>
    <div class="abs" style="left:105px;top:21px;width:92px">
      <div class="kicker" style="color:#333">Praxis</div>
      <div class="h2" style="font-size:3.6px">Dr. med. Adrian Sollberger</div>
      <p class="body" style="font-size:1.6px;margin-top:1px">Guten Tag<br>Ich freue mich, dass Sie Ihr Weg auf die Seiten der "Dermatologie am Lindwarte" geführt hat!<br>Es ist mir ein großes Anliegen, für Sie zu all Ihren Problemen an der Haut ein vertrauensvoller Ansprechpartner zu sein. Ich möchte Sie individuell als kompetenter Arzt sowie empathischer Mensch beraten und gemeinsam mit Ihnen die geeignete Therapie auswählen. Bei meiner Arbeit lege ich Wert auf eine wissenschaftlich aktuelle und leitliniengerechte Therapie, lasse aber immer Elemente der alternativen Medizin einfließen. Dies gehört für mich zur integrativen Behandlung auf der Grundlage eines ganzheitlichen Menschenbildes.</p>
    </div>
    <div class="btn-out" style="left:105px;top:86px;width:37px;height:6px;color:#aaa">Online Termine <span>→</span></div>
    <div class="pic" style="left:202px;top:25px;width:63px;height:55px;background:linear-gradient(135deg,#eef0f1,#c5ccd1 45%,#e3d1bb)" role="img" aria-label="Patientin bei einer Behandlung im hellen Behandlungsraum"></div>
    <div class="abs" style="left:45px;top:105px;width:222px;height:.6px;background:#9bb08a"></div>
    <div class="vita" style="left:46px;top:124px;width:90px">
      <p><b>Vita</b><br>Inhaber "Dermatologie am Lindwarte" seit 01/2025<br>Facharzt Dermatologie und Venerologie<br>Spezialist für Dermatochirurgie<br>und Lasermedizin</p>
      <p>Stv. Chefarzt Dermatologie 01/2020 – 12/2024<br>der Aarhof Kliniken AG in Olten</p>
      <p>Chefarzt Dermatologie 07/2018 – 06/2020<br>bei Talmed AG in Birrhof</p>
      <p>Leitender Oberarzt Dermatologie 01/2016 – 06/2018<br>Facharzt Dermatologie 08/2010 – 12/2015<br>der Aarhof Kliniken AG in Olten</p>
      <p>Promotion zum Dr. med. an der 11/2012<br>Universität Nordstadt (D)</p>
      <p>Weiterbildungsassistent Dermatologie 05/2005 – 06/2010<br>in der Hautklinik am Klinikum Nordstadt (D)<br>und an der Universitätshautklinik Westfeld (D)</p>
      <p>Studium der Humanmedizin 10/1998 – 06/2005<br>an der Universität Westfeld (D)<br>und im Kantonsspital Seewald</p>
    </div>
    <div class="vita" style="left:174px;top:124px;width:94px">
      <p><b>Mitglied in Fachgesellschaften</b><br>VHV (Verband für Haut- und Venenheilkunde)<br>HKB (Hautkreis Basel)<br>ÄGR (Ärztegilde Rheinknie / Regionale Ärzterunde)<br>VLA (Verein für medizinische Laseranwendungen)<br>RÄD (Runde ästhetische Dermatologie &amp; Hautpflege)<br>DVN (Dermatologenverbund Nord)<br>AHC (Arbeitskreis Hautchirurgie)<br>FAI (Forum Allergie und klinische Immunologie)</p>
    </div>
  </section>

  <section class="abs faq">
    <div class="faq-q"><span>Was muss ich bei meinem Hautarztbesuch beachten?</span><span>×</span></div>
    <p class="faq-a">Nibh quisque suscipit fermentum netus nulla cras porttitor euismod nulla. Orci, dictumst nec aliquet id ullamcorper venenatis. Fermentum sulla craspor ttitore ismod nulla. Elit adipiscing proin quis est consectetur. Felis ultricies nisi, quis malesuada sem odio. Potentiborbi natoque amet amet, tincidunt ultricies et. Et nam rhoncus sit nullam diam tincidunt condimentum nullam.</p>
    <div class="faq-q"><span>Tempus magna risus interdum ultricies sed urna?</span><span>+</span></div>
    <div class="faq-q"><span>Augue in nibh urna volutpat mattis?</span><span>+</span></div>
    <div class="faq-q"><span>Eu egestas sed sed posuere ultrices ?</span><span>+</span></div>
    <div class="faq-q"><span>Elementum facilisi aliquam, nisi, orci vulputate?</span><span>+</span></div>
    <div class="faq-q"><span>Nibh at odio dolor etiam neque in vel id orci?</span><span>+</span></div>
    <div class="faq-q" style="border-bottom:.4px solid var(--line)"><span>Non dolor at velit lorem erat maecenas?</span><span>+</span></div>
  </section>

  <section>
    <div class="abs center" style="left:0;top:925px;width:314px">
      <div class="kicker">Praxis</div>
      <div class="h2" style="font-size:3.4px">Öffnungszeiten</div>
    </div>
    <div class="nav-dot" style="left:40px;top:941px"></div>
    <div class="nav-dot" style="left:265px;top:941px"></div>
    <div class="tile" style="left:43px">Montag<br>8:30–17:00</div>
    <div class="tile" style="left:88px">Dienstag<br>8:30–17:00</div>
    <div class="tile" style="left:133px">Mittwoch<br>8:30–17:00</div>
    <div class="tile" style="left:178px">Donnerstag<br>8:30–17:00</div>
    <div class="tile" style="left:223px">Freitag<br>8:30–17:00</div>
    <div class="abs kicker center" style="left:0;top:967px;width:314px">Online Termine</div>
  </section>

  <section class="band" style="top:995px;height:117px">
    <div class="abs center" style="left:0;top:7px;width:308px">
      <div class="kicker" style="color:#333">Blog</div>
      <div class="h2" style="font-size:3.2px">Unsere neuesten und beliebtesten Tipps und Tricks für Sie</div>
    </div>
  </section>
  <article class="post" style="left:43px">
    <div class="p-img" style="background:linear-gradient(135deg,#e8e9ea,#8799ad 55%,#4e5866)" role="img" aria-label="Patient im Gespräch in der Praxis"></div>
    <div class="date">17<br>Nov</div>
    <h4>Formen des Haarausfalls</h4>
    <p>In der Haarsprechstunde widmen wir uns vor allem dem anlagebedingten Haarausfall (androgenetische Alopezie, AGA) …</p>
    <div class="more">mehr</div>
  </article>
  <article class="post" style="left:119px">
    <div class="p-img" style="background:linear-gradient(135deg,#c8342c,#e9922b 40%,#6f9b3a 75%,#3a2c5a)" role="img" aria-label="Frisches Obst und Gemüse"></div>
    <div class="date">18<br>Nov</div>
    <h4>Gesunde Gewohnheiten 101: Ein Leitfaden zur Stärkung Ihres Immunsystems</h4>
    <p>Entdecken Sie die beliebtesten und effektivsten Strategien zur Aufrechterhaltung einer robusten Immungesundheit.</p>
    <div class="more">mehr</div>
  </article>
  <article class="post" style="left:195px">
    <div class="p-img" style="background:linear-gradient(135deg,#6e8a55,#e6e3de 45%,#b9967c)" role="img" aria-label="Ärztin untersucht den Rücken einer Patientin"></div>
    <div class="date">19<br>Nov</div>
    <h4>Pigmentflecken</h4>
    <p>Die Behandlung von Sonnenflecken, Melasma und entzündlich bedingten Pigmentverschiebungen bedarf großer …</p>
    <div class="more">mehr</div>
  </article>

  <footer class="footer">
    <div class="fcol" style="left:43px"><div class="t">Menu</div>Home<br>Über Uns<br>Leistungen<br>Blog<br>Kontakt</div>
    <div class="fcol" style="left:98px"><div class="t">Links</div>Gesundheitstipps<br>FAQs<br>Versicherungsinformationen<br>Patientenressourcen<br>Karriere<br>Labor<br>Allgemeine<br>Geschäftsbedingungen<br>Datenschutzrichtlinie</div>
    <div class="fcol" style="left:165px"><div class="t">Kalender</div>Events<br>Programs</div>
    <div class="fcol" style="left:222px;top:9px"><div class="t">Connect With Us</div></div>
    <div class="social"><i></i><i></i><i></i><i></i><i></i></div>
    <div class="abs" style="left:43px;top:75px;width:240px;height:.4px;background:#6f8a58"></div>
    <div class="fcol" style="left:43px;top:78px;font-size:1.6px">© 2025 dermatologie-lindwarte</div>
  </footer>
  <div class="flogo"><div class="logo"><span class="dot"></span><span>Dermatologie<small>am Lindwarte</small></span></div></div>

</main>
</body>
</html>
```